Modernise Business Card

Our company has been operating for 10 years. With the start of the new decade we are looking to refresh our business card design. We manufacture a range of industrial product shipping to customers internationally. A copy of our current card, both sides, is attached. We are looking for a mature professional appearance.

```html
<!DOCTYPE html>
<html lang="en">
<head>
<meta charset="utf-8">
<title>Vantrel Business Card</title>
<link rel="stylesheet" href="https://fonts.googleapis.com/css2?family=Rajdhani:wght@500;700&family=Montserrat:wght@300;700&family=Noto+Serif&family=Signika:wght@400&display=swap">
<style>
  :root {
    --backdrop: #3b4244;
    --card-dark: #1d1f21;
    --panel: #3d4042;
    --blue: #1aa6df;
    --blue-light: #27b6e6;
    --blue-deep: #079ada;
    --blue-faint: #7cc4ec;
    --white: #ffffff;
    --ink: #1b1d1f;
  }
  * { margin: 0; padding: 0; box-sizing: border-box; }
  html, body { width: 1200px; height: 1149px; overflow: hidden; background: var(--backdrop); }
  .card {
    position: absolute; left: 277px; width: 655px; height: 374px;
    background: var(--card-dark); overflow: hidden;
  }
  .card-front { top: 130px; background: linear-gradient(135deg, #232629 0%, #1c1e20 60%, #191b1d 100%); }
  .card-back { top: 622px; }
  .card svg.shapes { position: absolute; left: 0; top: 0; }
  .brand-name {
    position: absolute; left: 267px; top: 40px; width: 350px;
    font-family: 'Rajdhani', sans-serif; font-weight: 700; font-size: 82px;
    line-height: 1; color: var(--blue); text-align: right; letter-spacing: 1px;
  }
  .services {
    position: absolute; left: 289px; width: 300px; top: 156px;
    font-family: 'Rajdhani', sans-serif; font-weight: 500; color: var(--white);
    text-align: center; font-size: 34px; line-height: 44px;
  }
  .services .spaced { letter-spacing: 3px; }
  .services .dash {
    display: inline-block; width: 32px; height: 6px; background: var(--blue);
    vertical-align: middle; margin: 0 10px 4px;
  }
  .web-front {
    position: absolute; left: 346px; top: 321px; width: 309px; height: 38px;
    font-family: 'Noto Serif', serif; font-size: 19px; color: var(--ink);
    text-align: center; line-height: 38px; letter-spacing: 0.5px;
  }
  .brand-faint {
    position: absolute; left: 63px; top: 192px; transform: translate(-50%, -50%) rotate(-90deg);
    font-family: 'Rajdhani', sans-serif; font-weight: 700; font-size: 76px;
    line-height: 1; color: var(--blue-faint); opacity: 0.75; white-space: nowrap; letter-spacing: 1px;
  }
  .person-name {
    position: absolute; left: 262px; top: 33px; width: 393px; height: 72px;
    font-family: 'Montserrat', sans-serif; font-size: 34px; color: var(--white);
    line-height: 72px; text-align: center; letter-spacing: 0.5px;
  }
  .person-name .first { font-weight: 300; }
  .person-name .last { font-weight: 700; }
  .contact {
    position: absolute; font-family: 'Signika', sans-serif; color: var(--white);
    font-size: 13px; line-height: 17.5px; white-space: nowrap;
  }
  .contact-address { left: 388px; top: 127px; }
  .contact-phone { left: 413px; top: 213px; font-size: 14px; line-height: 20px; }
  .contact-web { left: 428px; top: 290px; font-size: 14px; line-height: 20px; }
  .indent { padding-left: 7px; }
</style>
</head>
<body>

<section class="card card-front">
  <svg class="shapes" width="655" height="374" viewBox="0 0 655 374">
    <defs>
      <linearGradient id="blueFront" x1="0" y1="0" x2="0" y2="1">
        <stop offset="0" stop-color="#29b5e6"/>
        <stop offset="1" stop-color="#079ada"/>
      </linearGradient>
    </defs>
    <polygon class="accent-top" points="0,20 54,20 97,136 0,136" fill="url(#blueFront)"/>
    <polygon class="accent-wedge" points="2,164 107,164 171,343" fill="url(#blueFront)"/>
    <polygon class="accent-base" points="0,186 0,355 154,355" fill="url(#blueFront)"/>
    <polygon class="web-icon-tab" points="271,321 321,321 339,359 289,359" fill="var(--blue)"/>
    <polygon class="web-band" points="327,321 655,321 655,359 346,359" fill="var(--blue)"/>
    <g class="globe-icon" fill="none" stroke="#1b1d1f" stroke-width="1.6">
      <circle cx="306" cy="340" r="11" fill="#1b1d1f"/>
      <g stroke="#1aa6df" stroke-width="1.2">
        <ellipse cx="306" cy="340" rx="4.5" ry="10"/>
        <line x1="296" y1="340" x2="316" y2="340"/>
        <line x1="298" y1="334" x2="314" y2="334"/>
        <line x1="298" y1="346" x2="314" y2="346"/>
        <line x1="306" y1="330" x2="306" y2="350"/>
      </g>
    </g>
  </svg>
  <div class="brand-name">VANTREL</div>
  <div class="services">
    <div>Hydraulic Adapters</div>
    <div><span class="dash"></span>Hose Fittings<span class="dash"></span></div>
    <div class="spaced">Quick Couplings</div>
  </div>
  <div class="web-front">www.vantrelfittings .com</div>
</section>

<section class="card card-back">
  <svg class="shapes" width="655" height="374" viewBox="0 0 655 374">
    <defs>
      <linearGradient id="blueBack" x1="0" y1="0" x2="0" y2="1">
        <stop offset="0" stop-color="#27b6e6"/>
        <stop offset="1" stop-color="#079ada"/>
      </linearGradient>
    </defs>
    <polygon class="side-panel" points="0,0 212,0 318,374 0,374" fill="url(#blueBack)"/>
    <polygon class="top-bar" points="232,0 655,0 655,13 235,13" fill="var(--blue)"/>
    <polygon class="bottom-bar" points="338,361 655,361 655,374 341,374" fill="var(--blue)"/>
    <polygon class="name-panel" points="242,33 655,33 655,105 262,105" fill="var(--panel)"/>

    <polygon class="icon-tab" points="269,122 334,122 353,184 287,184" fill="var(--blue)"/>
    <polygon class="info-panel" points="349,122 655,122 655,184 367,184" fill="var(--panel)"/>
    <polygon class="icon-tab" points="291,201 358,201 377,263 310,263" fill="var(--blue)"/>
    <polygon class="info-panel" points="372,201 655,201 655,263 390,263" fill="var(--panel)"/>
    <polygon class="icon-tab" points="315,278 382,278 402,341 334,341" fill="var(--blue)"/>
    <polygon class="info-panel" points="395,278 655,278 655,341 413,341" fill="var(--panel)"/>

    <g class="home-icon" fill="#ffffff">
      <polygon points="310,144 297,155 300,155 310,147 320,155 323,155"/>
      <polygon points="301,155 310,148 319,155 319,166 313,166 313,159 307,159 307,166 301,166"/>
      <rect x="316" y="145" width="3" height="6"/>
    </g>
    <g class="phone-icon" fill="none" stroke="#ffffff" stroke-width="3.2" stroke-linecap="round">
      <path d="M336,222 C329,226 329,238 336,245"/>
      <line x1="336" y1="222" x2="339" y2="226"/>
      <line x1="336" y1="245" x2="339" y2="242"/>
    </g>
    <g class="globe-icon" fill="none" stroke="#ffffff" stroke-width="1.6">
      <circle cx="357" cy="310" r="13"/>
      <ellipse cx="357" cy="310" rx="5.5" ry="13"/>
      <line x1="344" y1="310" x2="370" y2="310"/>
      <line x1="346" y1="303" x2="368" y2="303"/>
      <line x1="346" y1="317" x2="368" y2="317"/>
      <line x1="357" y1="297" x2="357" y2="323"/>
    </g>
  </svg>
  <div class="brand-faint">VANTREL</div>
  <div class="person-name"><span class="first">ALAN</span> <span class="last">BRECKER</span></div>
  <div class="contact contact-address">
    <div>1208- 4,Lian Feng Building</div>
    <div class="indent">316 Haoyuan Road,Beilun District</div>
    <div class="indent">Ningbo 315800 China</div>
  </div>
  <div class="contact contact-phone">
    <div>China: +86 150 2273 0914</div>
    <div class="indent">Australia: +61 402 118 735</div>
  </div>
  <div class="contact contact-web">
    <div>abrecker@vantrelfittings.com</div>
    <div class="indent">www.vantrelfittings .com</div>
  </div>
</section>

</body>
</html>
```